Professional Services/Construction Management (Millwork) Biz Cards

We've decided on a logo and have our color palette set, now we want to design some very professional looking cards that make a strong first impression - they'll reflect our tagline (that we're going to put on the back: Innovative. Professional. Leaders.

The example business card shows generally the direction we've been thinking of going for the back side - **but we're open to other ideas**

Target Market(s)

The cards should target more high-end (wealthy) owners and general contracting companies. We want them to convey a strong first impression - in a professional and not garish way.

Industry/Entity Type

Construction Company

Contact Information for Business Card

There needs to be a place for our company contractor's license number and business address. We want to also have people's names, titles, phone number, email address. The back can be the logo, tagline and web address

Requirements
Must have
• follow our color palette
Nice to have
• Font & Styles should compliment the Harbor Joinery fonts, but not necessarily match exactly

```html
<!DOCTYPE html>
<html lang="en">
<head>
<meta charset="utf-8">
<title>Harbor Joinery Business Cards</title>
<link href="https://fonts.googleapis.com/css2?family=Arimo:wght@400;700&display=swap" rel="stylesheet">
<style>
  :root {
    --ink: #0b0b0b;
    --paper: #f4f4f4;
    --mark: #2e2b2b;
    --ring: #4a4747;
    --backdrop: #e4e2df;
    --white: #ffffff;
  }
  html, body {
    margin: 0;
    width: 1200px;
    height: 902px;
    overflow: hidden;
    background: var(--backdrop);
    font-family: "Arimo", Arial, sans-serif;
  }
  .card {
    position: absolute;
    width: 540px;
    height: 310px;
    background: var(--paper);
    box-shadow: 0 14px 30px rgba(0,0,0,0.25);
    overflow: hidden;
  }
  .card svg.bands { position: absolute; inset: 0; }
  .card--front { left: 90px; top: 70px; }
  .card--back { left: 570px; top: 500px; }

  .brand-mark {
    position: absolute;
    width: 190px;
    height: 190px;
    border-radius: 50%;
    background: var(--mark);
    box-shadow: 0 0 0 7px var(--white), 0 0 0 12px var(--ring);
    display: flex;
    align-items: center;
    justify-content: center;
    text-align: center;
  }
  .brand-name {
    color: var(--white);
    font-weight: 700;
    font-size: 25px;
    line-height: 1.1;
    letter-spacing: 1px;
    text-transform: uppercase;
  }
  .card--front .brand-mark { left: 175px; top: 50px; }
  .card--back .brand-mark { left: 70px; top: 90px; width: 170px; height: 170px; }
  .card--back .brand-name { font-size: 22px; }

  .service-line {
    position: absolute;
    right: 28px;
    top: 38px;
    font-size: 34px;
    color: var(--ink);
  }
  .contact {
    position: absolute;
    right: 22px;
    top: 140px;
    text-align: right;
    color: var(--white);
  }
  .contact__name { font-size: 27px; font-weight: 700; line-height: 1; }
  .contact__title { font-size: 15px; font-weight: 700; margin: 3px 0 14px; }
  .contact__row {
    font-size: 13px;
    line-height: 19px;
    display: flex;
    justify-content: flex-end;
    align-items: center;
    gap: 8px;
  }
  .contact__row svg { width: 12px; height: 12px; flex: none; }
  .license {
    position: absolute;
    left: 24px;
    bottom: 16px;
    color: var(--white);
    font-size: 19px;
    font-weight: 700;
  }
</style>
</head>
<body>

<section class="card card--front" aria-label="Card front">
  <svg class="bands" viewBox="0 0 540 310" preserveAspectRatio="none">
    <polygon points="0,0 540,0 540,100 0,150" fill="var(--ink)"/>
  </svg>
  <div class="brand-mark"><span class="brand-name">Harbor<br>Joinery</span></div>
</section>

<section class="card card--back" aria-label="Card back">
  <svg class="bands" viewBox="0 0 540 310" preserveAspectRatio="none">
    <path d="M0,255 L225,225 Q250,140 330,128 L540,100 L540,310 L0,310 Z" fill="var(--ink)"/>
  </svg>
  <div class="service-line">Professional Services</div>
  <div class="brand-mark"><span class="brand-name">Harbor<br>Joinery</span></div>
  <div class="contact">
    <div class="contact__name">Ethan Marsh</div>
    <div class="contact__title">Project Engineer</div>
    <div class="contact__row">555 010 4821
      <svg viewBox="0 0 12 12"><rect width="12" height="12" rx="2" fill="var(--white)"/><path d="M3 3h2l1 2-1 1q1 2 2 2l1-1 2 1v2q-6 0-7-7z" fill="var(--ink)"/></svg>
    </div>
    <div class="contact__row">harborjoinery@mail.com
      <svg viewBox="0 0 12 12"><rect width="12" height="12" rx="2" fill="var(--white)"/><rect x="2.5" y="3.5" width="7" height="5" fill="none" stroke="var(--ink)"/><path d="M2.5 3.5l3.5 3 3.5-3" fill="none" stroke="var(--ink)"/></svg>
    </div>
    <div class="contact__row">118 Ferry Lane, Milton, OR 97000
      <svg viewBox="0 0 12 12"><rect width="12" height="12" rx="2" fill="var(--white)"/><path d="M6 10L3.5 6a2.5 2.5 0 1 1 5 0z" fill="var(--ink)"/></svg>
    </div>
  </div>
  <div class="license">Lic No: 730418265</div>
</section>

</body>
</html>
```